Card design for home renovation company

We are a home renovation company looking for a card design with new logo. We look after every aspect of home renovation from design stage to completion.

Company name is, Brightwater Renovations

Target Market(s)

People wanting to have a home designed and built or renovated

Industry/Entity Type

Construction / Home Renovations

Contact Information for Business Card

Company name: Brightwater Renovations. Phone, email, website

Font styles to use
Serif
Sans Serif

Colors

Designer to choose only greyscale colors for use in the design.

Requirements
Must have
• Double sided card.
Nice to have
• A roofline logo integrated into the name

```html
<!DOCTYPE html>
<html lang="en">
<head>
<meta charset="utf-8">
<title>Brightwater Renovations – Business Card</title>
<link rel="stylesheet" href="https://fonts.googleapis.com/css2?family=Archivo:ital,wght@0,400;0,700;1,400&display=swap">
<style>
  :root {
    --backdrop: #525252;
    --card-dark: #0b0b0b;
    --card-light: #ececec;
    --ink-light: #ededed;
    --ink-dark: #0d0d0d;
  }
  * { margin: 0; padding: 0; box-sizing: border-box; }
  html, body {
    width: 1200px;
    height: 800px;
    overflow: hidden;
    background: var(--backdrop);
    font-family: "Archivo", Arial, sans-serif;
  }
  .canvas {
    position: relative;
    width: 1200px;
    height: 800px;
    display: flex;
    align-items: center;
    justify-content: center;
    gap: 60px;
  }
  .card {
    position: relative;
    width: 300px;
    height: 464px;
  }
  .card--front {
    background: var(--card-dark);
    color: var(--ink-light);
  }
  .card--back {
    background: var(--card-light);
    color: var(--ink-dark);
  }
  .holder {
    position: absolute;
    left: 36px;
    top: 48px;
  }
  .holder__name {
    font-weight: 700;
    font-size: 20px;
    line-height: 1.1;
    letter-spacing: 0.1px;
  }
  .holder__role {
    font-style: italic;
    font-weight: 400;
    font-size: 13.5px;
    margin-top: 2px;
  }
  .front-brand {
    position: absolute;
    left: 36px;
    top: 196px;
    display: flex;
    align-items: center;
    gap: 8px;
    font-weight: 700;
    font-size: 13px;
  }
  .brand-square {
    width: 10px;
    height: 10px;
    background: currentColor;
  }
  .address {
    position: absolute;
    left: 36px;
    top: 234px;
    font-size: 14px;
    line-height: 1.25;
  }
  .contact {
    position: absolute;
    left: 36px;
    top: 394px;
    font-size: 14px;
    line-height: 1.6;
  }
  .wordmark {
    position: absolute;
    left: 28px;
    bottom: 26px;
    display: flex;
    align-items: flex-start;
    gap: 10px;
  }
  .wordmark__name {
    font-weight: 700;
    font-size: 30px;
    line-height: 0.98;
    letter-spacing: -0.3px;
  }
  .wordmark .brand-square {
    width: 16px;
    height: 16px;
    margin-top: 6px;
  }
</style>
</head>
<body>
  <main class="canvas">
    <section class="card card--front" aria-label="Card front">
      <div class="holder">
        <p class="holder__name">Mara Ellison</p>
        <p class="holder__role">Founder + CEO</p>
      </div>
      <div class="front-brand">
        <span class="brand-square"></span>
        <span>Brightwater Renovations</span>
      </div>
      <address class="address" style="font-style: normal;">
        Fernhill Chapel Rooms<br>
        Millbrook Rd Ashdale AD14 7QP
      </address>
      <div class="contact">
        <p>(123) 0987 654</p>
        <p>hello@brightwaterreno.com</p>
      </div>
    </section>

    <section class="card card--back" aria-label="Card back">
      <div class="wordmark">
        <p class="wordmark__name">Brightwater<br>Renovations</p>
        <span class="brand-square"></span>
      </div>
    </section>
  </main>
</body>
</html>
```